Corvena Hotel, city center modern minimal hotel operating all year round, on Rhodes island Greece

city, modern ,all year operating hotel

Target Market(s)

tourists, business agents

Industry/Entity Type

tourism

Coding

Coded - Design and coding required

Number of Pages Required

2 page

Requirements
Must have
• room type photos and descriptions, amenities individual listing (graphic), comments sections, map driving location details
Nice to have
• gallery section, modern and minimal design, amenities section, individual room type descriptions, photos and facilities

```html
<!DOCTYPE html>
<html lang="en">
<head>
<meta charset="utf-8">
<title>Corvena Hotel – Rooms &amp; Rates</title>
<link rel="stylesheet" href="https://fonts.googleapis.com/css2?family=Raleway:wght@400;500;600;700&family=Work+Sans:wght@300;400;500&display=swap">
<style>
:root{
  --green:#173f1f;
  --nav-green:#1a5c28;
  --blue:#2a72c9;
  --field:#a9cdf0;
  --title-blue:#2c73c4;
  --ink:#3a3a3a;
  --ink-soft:#555;
  --page:#f1f1f1;
  --white:#fff;
}
*{margin:0;padding:0;box-sizing:border-box}
html,body{width:963px;height:1200px;overflow:hidden;background:var(--page);font-family:"Work Sans",sans-serif;color:var(--ink)}
.canvas{position:relative;width:963px;height:1200px;overflow:hidden}
.hero-photo{position:absolute;left:0;top:0;width:963px;height:415px;
  background:linear-gradient(100deg,#b9b2a8 0%,#d9d3cb 22%,#cbc2b6 45%,#dcdfe3 62%,#b8cbd8 78%,#9fb6c6 100%)}
.brand{position:absolute;left:154px;top:57px;width:154px;height:41px;background:var(--white);display:flex;align-items:center;gap:7px;padding-left:9px}
.brand-mark{width:18px;height:18px;background:var(--green)}
.brand-name{font-family:"Raleway",sans-serif;font-weight:500;font-size:17px;color:var(--green);letter-spacing:.5px}
.login{position:absolute;left:762px;top:44px;font-size:11px;color:var(--white)}
.nav{position:absolute;top:71px;left:0;height:14px;font-size:10.5px;color:var(--white)}
.nav a{position:absolute;top:0;white-space:nowrap;color:var(--white);text-decoration:none;line-height:14px}
.nav .active{background:var(--nav-green);width:99px;text-align:center}
.book-now{position:absolute;left:728px;top:66px;width:81px;height:23px;border:1.5px solid var(--white);color:var(--white);font-size:11px;display:flex;align-items:center;justify-content:center}
.page-title{position:absolute;left:154px;top:277px;width:224px;height:76px;background:var(--white)}
.page-title h1{position:absolute;left:19px;top:44px;font-family:"Raleway",sans-serif;font-weight:400;font-size:21px;color:var(--title-blue)}
.panel{position:absolute;left:154px;top:364px;width:655px;height:630px;background:var(--white)}
.panel h2{position:absolute;left:41px;top:24px;font-family:"Work Sans",sans-serif;font-weight:400;font-size:15px;color:var(--ink)}
.search{position:absolute;left:41px;top:73px;display:flex;gap:2px;height:24px}
.field{width:118px;background:var(--field);font-size:7.5px;color:#222;display:flex;align-items:center;justify-content:space-between;padding:0 5px}
.field svg{width:9px;height:9px}
.search-btn{width:92px;background:var(--blue);color:var(--white);font-size:11px;display:flex;align-items:center;justify-content:center}
.room{position:absolute;left:41px;width:575px;height:114px}
.room-photo{position:absolute;left:0;top:0;width:160px;height:113px}
.room-info{position:absolute;left:177px;top:0}
.room-info h3{font-family:"Raleway",sans-serif;font-weight:700;font-size:13px;color:var(--ink-soft);margin-top:2px}
.room-info p{font-size:7.3px;color:#333;margin-top:8px}
.room-info ul{list-style:none;margin-top:10px;font-size:7.3px;color:#333;line-height:11.5px}
.room-info li{position:relative;padding-left:13px}
.room-info li::before{content:"";position:absolute;left:0;top:4px;width:3.5px;height:3.5px;border-radius:50%;background:#333}
.amenities{display:flex;gap:11px;margin-top:12px}
.amenities svg{width:16px;height:16px;fill:none;stroke:#333;stroke-width:1.1;stroke-linecap:round;stroke-linejoin:round}
.rate{position:absolute;left:481px;top:22px;width:94px;text-align:center}
.rate .from{font-size:7.5px;color:#444}
.rate .price{font-family:"Raleway",sans-serif;font-size:24px;font-weight:400;color:#444;margin-top:3px}
.rate .more{margin-top:8px;height:24px;background:var(--blue);color:var(--white);font-size:10.5px;display:flex;align-items:center;justify-content:center}
.footer{position:absolute;left:0;top:1038px;width:963px;height:162px;background:var(--green);color:var(--white)}
.footer-col{position:absolute;top:44px}
.footer-col::before{content:"";display:block;width:22px;height:2px;background:var(--white);margin-bottom:14px}
.footer-col h4{font-weight:400;font-size:14px}
.footer-col .phone{font-family:"Raleway",sans-serif;font-weight:700;font-size:12.5px;margin-top:3px}
.footer-col .copy{font-size:10.5px;margin-top:1px}
.socials{display:flex;gap:13px;margin-top:6px}
.socials span{width:13px;height:13px;border-radius:50%;background:var(--white)}
.chat{position:absolute;left:816px;top:1149px;width:134px;height:37px;border:1px solid #3e6446;border-radius:20px;display:flex;align-items:center;justify-content:center;gap:8px;color:var(--white);font-size:11.5px}
.chat svg{width:15px;height:15px}
</style>
</head>
<body>
<div class="canvas">
<svg width="0" height="0" style="position:absolute">
  <defs>
    <symbol id="i-ac" viewBox="0 0 16 16"><path d="M8 1v14M2 4.5l12 7M2 11.5l12-7M6.5 2.2L8 3.5l1.5-1.3M6.5 13.8L8 12.5l1.5 1.3"/></symbol>
    <symbol id="i-wifi" viewBox="0 0 16 16"><path d="M1.5 5.5a9 9 0 0 1 13 0M3.5 8a6 6 0 0 1 9 0M5.5 10.5a3 3 0 0 1 5 0"/><circle cx="8" cy="13" r=".6"/></symbol>
    <symbol id="i-tv" viewBox="0 0 16 16"><rect x="2" y="5" width="12" height="9"/><rect x="4" y="7" width="8" height="5"/><path d="M5.5 1.5L8 5l2.5-3.5"/></symbol>
    <symbol id="i-safe" viewBox="0 0 16 16"><rect x="1.5" y="2.5" width="13" height="11"/><rect x="3.5" y="4.5" width="9" height="7"/><circle cx="8" cy="8" r="1.8"/></symbol>
    <symbol id="i-bar" viewBox="0 0 16 16"><path d="M3 1.5h2v3l1.5 2v8h-5v-8l1.5-2zM9.5 7h5c0 2.5-1 3.5-2.5 3.5S9.5 9.5 9.5 7zM12 10.5v4M10.5 14.5h3"/></symbol>
    <symbol id="i-phone" viewBox="0 0 16 16"><path d="M3 1.5l3 3-1.5 2a9 9 0 0 0 5 5l2-1.5 3 3-2 2C7 14 2 9 1 3.5z"/></symbol>
    <symbol id="i-dine" viewBox="0 0 16 16"><path d="M2.5 1.5v5a2 2 0 0 0 4 0v-5M4.5 1.5v13M11 14.5v-13c2 1 3 3 3 6h-3"/></symbol>
    <symbol id="i-desk" viewBox="0 0 16 16"><rect x="3" y="1.5" width="10" height="10"/><path d="M1.5 11.5h13M4 11.5v3M12 11.5v3M5 4h6"/></symbol>
    <symbol id="i-shower" viewBox="0 0 16 16"><path d="M2 14.5V7a6 6 0 0 1 12 0H2M5 10v1M8 10v1M11 10v1M6.5 13v1M9.5 13v1"/></symbol>
    <symbol id="i-bath" viewBox="0 0 16 16"><path d="M1.5 8h13l-1.5 5h-10zM4 8V3.5a2 2 0 0 1 3.5-1M4 13l-1 2M12 13l1 2"/></symbol>
    <symbol id="i-bed" viewBox="0 0 16 16"><path d="M2 14.5V2h12v12.5M2 6h12M5 2v4"/></symbol>
    <symbol id="i-cal" viewBox="0 0 10 10"><rect x=".8" y="1.5" width="8.4" height="7.7" fill="none" stroke="#444" stroke-width=".8"/><path d="M.8 3.5h8.4M3 .5v2M7 .5v2" stroke="#444" stroke-width=".8"/></symbol>
    <symbol id="i-step" viewBox="0 0 10 10"><path d="M5 .5L8 4H2zM5 9.5L2 6h6z" fill="#333"/></symbol>
  </defs>
</svg>

<div class="hero-photo" role="img" aria-label="Bright hotel dining room with bookshelves, framed floral print, glass table and large windows overlooking the sea"></div>

<header>
  <div class="brand"><span class="brand-mark"></span><span class="brand-name">Corvena Hotel</span></div>
  <a class="login">Log In</a>
  <nav class="nav">
    <a style="left:374px">Home</a>
    <a class="active" style="left:416px">Rooms &amp; Rates</a>
    <a style="left:530px">Activities</a>
    <a style="left:599px">About Us</a>
    <a style="left:670px">Contact</a>
  </nav>
  <div class="book-now">Book Now</div>
</header>

<div class="page-title"><h1>Rooms &amp; Rates</h1></div>

<main class="panel">
  <h2>Our Rooms</h2>
  <div class="search">
    <div class="field">Check-In<svg><use href="#i-cal"/></svg></div>
    <div class="field">Check-Out<svg><use href="#i-cal"/></svg></div>
    <div class="field">1 Adults<svg><use href="#i-step"/></svg></div>
    <div class="field">0 Kids<svg><use href="#i-step"/></svg></div>
    <div class="search-btn">Search</div>
  </div>

  <article class="room" style="top:136px">
    <div class="room-photo" role="img" aria-label="White pillows on a freshly made bed" style="background:linear-gradient(135deg,#8a7060 0%,#d8d4d4 40%,#eeeef3 70%,#c9c8d2 100%)"></div>
    <div class="room-info">
      <h3>Junior Suite</h3>
      <p>Our Junior Suites offer breathtaking views of the city skyline.</p>
      <ul><li>Size: 260 sq ft</li><li>Beds: 2 Double(s)</li></ul>
      <div class="amenities">
        <svg><use href="#i-ac"/></svg><svg><use href="#i-wifi"/></svg><svg><use href="#i-tv"/></svg><svg><use href="#i-safe"/></svg><svg><use href="#i-bar"/></svg><svg><use href="#i-phone"/></svg><svg><use href="#i-dine"/></svg><svg><use href="#i-desk"/></svg>
      </div>
    </div>
    <div class="rate"><div class="from">From</div><div class="price">$250</div><div class="more">More Info</div></div>
  </article>

  <article class="room" style="top:300px">
    <div class="room-photo" role="img" aria-label="Bedside table with lamp and teacup beside white pillows" style="background:linear-gradient(120deg,#2a211d 0%,#3d302b 40%,#d9d6d3 65%,#f3f2f1 100%)"></div>
    <div class="room-info">
      <h3>Standard Room</h3>
      <p>Our Standard Rooms are the perfect combination of function and comfort.</p>
      <ul><li>Size: 230 sq ft</li><li>Beds: 1 Double(s)</li></ul>
      <div class="amenities">
        <svg><use href="#i-ac"/></svg><svg><use href="#i-wifi"/></svg><svg><use href="#i-tv"/></svg><svg><use href="#i-safe"/></svg><svg><use href="#i-bar"/></svg><svg><use href="#i-phone"/></svg><svg><use href="#i-dine"/></svg>
      </div>
    </div>
    <div class="rate"><div class="from">From</div><div class="price">$150</div><div class="more">More Info</div></div>
  </article>

  <article class="room" style="top:465px">
    <div class="room-photo" role="img" aria-label="Bed with gold satin cushions and a bedside lamp" style="background:linear-gradient(120deg,#5a3a28 0%,#c9b89a 40%,#e6dcc6 60%,#f4f1ea 100%)"></div>
    <div class="room-info">
      <h3>Superior Room</h3>
      <p>Our Superior Rooms are comfortable, roomy and elegant.</p>
      <ul><li>Size: 280 sq ft</li><li>Beds: 1 King(s)</li></ul>
      <div class="amenities">
        <svg><use href="#i-ac"/></svg><svg><use href="#i-wifi"/></svg><svg><use href="#i-tv"/></svg><svg><use href="#i-safe"/></svg><svg><use href="#i-bar"/></svg><svg><use href="#i-shower"/></svg><svg><use href="#i-phone"/></svg><svg><use href="#i-bath"/></svg><svg><use href="#i-dine"/></svg><svg><use href="#i-bed"/></svg>
      </div>
    </div>
    <div class="rate"><div class="from">From</div><div class="price">$350</div><div class="more">More Info</div></div>
  </article>
</main>

<footer class="footer">
  <div class="footer-col" style="left:172px"><h4>Call us now to book</h4><div class="phone">1-800-555-0147</div></div>
  <div class="footer-col" style="left:396px"><h4>Follow us</h4><div class="socials"><span></span><span></span><span></span></div></div>
  <div class="footer-col" style="left:621px"><div class="copy">© 2023 by Corvena Hotel.</div></div>
</footer>

<div class="chat">
  <svg viewBox="0 0 16 16"><circle cx="8" cy="8" r="7.5" fill="#fff"/><circle cx="5" cy="8" r="1" fill="#173f1f"/><circle cx="8" cy="8" r="1" fill="#173f1f"/><circle cx="11" cy="8" r="1" fill="#173f1f"/></svg>
  <span>Let's Chat!</span>
</div>
</div>
</body>
</html>
```